Printing company needs a presentational catalogue, min. A5 format when closed, portrait or landscape

We need a corporate catalogue design for presentation of our company/services mainly to corporate customers. Our portfolio of services includes: offset printing, digital printing, screen printing, UV flatbed printing, direct UV printing on promotional items, textile printing (direct screen printing and heat transfer), computer cutting/plotting, CNC cutting, graphic design, setting for press; You can also use images of our products from our website www.velorantisk.si
We will adopt text later to the design so there should be some free space left for text. You should also determinate the typography of fonts for the category titles (offset printing, digital printing, etc...) and description of individual category.
Design should communicate in a way that we are there to solve our customer´s graphic problems and needs. Our new logo is attached. Catalogue colours should be matched with our new logo (kovan tisk). We will change our website soon (from velorantisk to kovantisk), so the catalogue should not be in colours of existent website design (blue and orange).

Target Market(s)

B2B customers (mixed field of work)

Industry/Entity Type

Printing

Requirements
Must have
• Our new company logo, but it should not step out too much (better to be small and discreet).
Nice to have
• Some images of products that we offer - they could be from our website www.velorantisk.si if you can integrate them well into design...

```html
<!DOCTYPE html>
<html lang="sl">
<head>
<meta charset="utf-8">
<title>Kovan Tisk – Grafično oblikovanje</title>
<link rel="stylesheet" href="https://fonts.googleapis.com/css2?family=Roboto:wght@300;400;700;900&family=Oswald:wght@700&family=Russo+One&display=swap">
<style>
  :root{
    --backdrop:#e4e4e4;
    --paper:#ececec;
    --paper-light:#f6f6f6;
    --ink:#3a3a3a;
    --ink-soft:#555;
    --red:#c0162c;
    --band:#4a4a4a;
    --band-edge:#d6d6d6;
    --frame:#f3f3f3;
  }
  *{box-sizing:border-box;margin:0;padding:0}
  html,body{width:1200px;height:1000px;overflow:hidden}
  body{background:var(--backdrop);font-family:"Roboto",Arial,sans-serif;position:relative}

  .catalogue-page{
    position:absolute;left:50px;top:111px;width:1100px;height:778px;
    background:linear-gradient(180deg,var(--paper-light),var(--paper));
    overflow:hidden;box-shadow:0 6px 20px rgba(0,0,0,.18);
  }

  .hero-photo{
    position:absolute;left:380px;top:0;width:720px;height:420px;
    background:
      linear-gradient(90deg,var(--paper-light) 0%,rgba(246,246,246,0) 30%),
      linear-gradient(180deg,rgba(236,236,236,0) 65%,var(--paper) 100%),
      linear-gradient(120deg,#d8d8d8 0%,#9aa3ad 30%,#2f5fb0 42%,#b9bcc0 52%,#c98a4a 66%,#7a8f5a 76%,#d96fa8 90%,#e9e9e9 100%);
  }

  .section-intro{position:absolute;left:48px;top:150px;width:360px}
  .section-title{
    font-family:"Russo One",Arial,sans-serif;font-weight:400;
    color:var(--red);font-size:25px;letter-spacing:.5px;
    padding-bottom:6px;border-bottom:1.5px solid var(--red);
  }
  .section-text{margin-top:10px;font-size:12px;line-height:1.45;color:var(--ink-soft)}

  .service-list{position:absolute;left:150px;top:445px;list-style:none}
  .service-list li{
    position:relative;padding-left:30px;font-weight:700;font-size:14px;
    line-height:19px;color:var(--ink);
  }
  .service-list li::before{
    content:"";position:absolute;left:0;top:5px;width:14px;height:9px;
    background:var(--red);clip-path:polygon(0 0,50% 55%,100% 0,100% 45%,50% 100%,0 45%);
  }

  .headline{
    position:absolute;right:40px;top:300px;font-size:52px;line-height:1;
    color:#fff;font-weight:300;text-shadow:0 1px 3px rgba(0,0,0,.25);
  }
  .headline strong{color:var(--red);font-weight:900;text-shadow:none}

  .band{position:absolute;left:0;top:0;width:1100px;height:778px}

  .tagline{
    position:absolute;left:600px;top:440px;display:flex;align-items:center;gap:20px;
    font-family:"Oswald",Arial,sans-serif;font-weight:700;font-size:28px;color:#5a5a5a;letter-spacing:.5px;
  }
  .tagline .mark{color:var(--red);font-size:64px;line-height:1}

  .work-title{
    position:absolute;left:40px;top:556px;font-size:62px;color:var(--red);
    font-weight:300;line-height:1;
  }
  .work-title strong{font-weight:900}

  .work-gallery{
    position:absolute;left:30px;top:656px;width:1040px;display:flex;gap:18px;
  }
  .work-item{
    flex:1;height:108px;background:var(--frame);padding:8px;
    box-shadow:0 3px 8px rgba(0,0,0,.45);
  }
  .work-item .photo{width:100%;height:100%}
  .photo-folder{background:linear-gradient(135deg,#dfe3e2,#2f5a4c 45%,#23473c)}
  .photo-label{background:linear-gradient(135deg,#e6ebf2,#c7d0e6 50%,#6f63b8)}
  .photo-art{background:linear-gradient(135deg,#eef0c6,#e08f63 45%,#d3382e 60%,#9ec28e)}
</style>
</head>
<body>
  <main class="catalogue-page">
    <div class="hero-photo" role="img" aria-label="Tiskarski stroj z modrim valjem in kolaž natisnjenih fotografij pokrajin in cvetov"></div>

    <svg class="band" viewBox="0 0 1100 778" aria-hidden="true">
      <path d="M0 618 Q560 598 1100 520 L1100 778 L0 778 Z" fill="var(--band-edge)"/>
      <path d="M0 640 Q560 620 1100 545 L1100 778 L0 778 Z" fill="var(--band)"/>
      <path d="M0 640 Q560 620 1100 545" fill="none" stroke="#8a8a8a" stroke-width="2"/>
    </svg>

    <section class="section-intro">
      <h1 class="section-title">GRAFIČNO OBLIKOVANJE</h1>
      <p class="section-text">Grafično oblikovanje predstavlja poleg same ideje prvi korak v smeri vizualne komunikacije z uporabnikom. Da neka ideja dobi privlačno obliko z določeno sporočilno vrednostjo, jo je potrebno najprej pravilno “oblikovati”. Vaše ideje lahko skupaj predebatiramo (vmes vam tudi svetujemo), v naslednjem koraku pa jih s pomočjo profesionalnih grafičnih programov približamo v realnost. Končna podoba neke tiskovine je namreč popolnoma odvisna od dobre oblikovalske zasnove, s tem pa v očeh končnega uporabnika tudi pridobi svojo pravo sporočilno vrednost. Pri nas vam lahko oblikujemo široko paleto tiskovin.</p>
    </section>

    <ul class="service-list">
      <li>vizitke in vabila</li>
      <li>letake, zloženke, plakate</li>
      <li>revije in kataloge</li>
      <li>ostalo po vaših željah</li>
    </ul>

    <h2 class="headline">Graphic <strong>Printing</strong></h2>

    <p class="tagline"><span class="mark">!</span>IMAGINATION HAS A SIMPLE PATH</p>

    <h2 class="work-title">Our <strong>Work</strong></h2>

    <div class="work-gallery">
      <figure class="work-item"><div class="photo photo-folder" role="img" aria-label="Odprta zelena mapa s potiskom"></div></figure>
      <figure class="work-item"><div class="photo photo-folder" role="img" aria-label="Zelena mapa z zlatim tiskom"></div></figure>
      <figure class="work-item"><div class="photo photo-folder" role="img" aria-label="Zelena mapa, detajl tiska"></div></figure>
      <figure class="work-item"><div class="photo photo-label" role="img" aria-label="Natisnjene nalepke na belem listu"></div></figure>
      <figure class="work-item"><div class="photo photo-art" role="img" aria-label="Barvni otroški plakat"></div></figure>
    </div>
  </main>
</body>
</html>
```